Reed & Vale NC grand opening (for BILLBOARD)

Advertising the grand opening of our cannabis/hemp shop in NC. We will sell all things hemp (flower, cartridges, disposables, edibles, creams, lotions, pet products etc...)

Requirements
Must have
• include, open starting Aug 1, but grand opening Aug 15th.
Nice to have
• Difference slogan ideas "Save some cash, buy our grass" "Find your perfect high at Reed & Vale cannabis store" "Experience Nature's Gift: Reed & Vale Cannabis Store"

```html
<!DOCTYPE html>
<html lang="en">
<head>
<meta charset="utf-8">
<title>Reed &amp; Vale – Grand Opening Billboard</title>
<link rel="stylesheet" href="https://fonts.googleapis.com/css2?family=Roboto:wght@700;900&family=Montserrat:wght@600;700&family=Kaushan+Script&display=swap">
<style>
  :root {
    --stage: #d6d6d6;
    --paper: #ffffff;
    --forest: #0b6b3a;
    --leaf: #7dc142;
    --lime: #b5d334;
    --pill: #a6cf2e;
    --slogan: #0e7a3a;
    --ink: #1e1e24;
    --muted: #454545;
    --horn-light: #d5287e;
    --horn-dark: #9c1447;
  }
  * { margin: 0; padding: 0; box-sizing: border-box; }
  html, body { width: 1200px; height: 523px; overflow: hidden; }
  body { background: var(--stage); position: relative; }

  .billboard {
    position: absolute; left: 20px; top: 91px;
    width: 1160px; height: 341px;
    background: var(--paper);
    overflow: hidden;
  }
  .billboard__decor { position: absolute; inset: 0; width: 100%; height: 100%; }

  .megaphone {
    position: absolute; top: 200px; width: 150px; height: 141px;
    border-radius: 40px 40px 0 0;
    background: linear-gradient(135deg, var(--horn-light), var(--horn-dark));
  }
  .megaphone--left { left: 118px; }
  .megaphone--right { right: 118px; }

  .brand-name {
    position: absolute; left: 0; right: 0; top: 48px;
    text-align: center;
    font: 700 62px/1 "Montserrat", sans-serif;
    color: var(--forest);
    letter-spacing: -1px;
  }
  .slogan {
    position: absolute; left: 0; right: 0; top: 142px;
    text-align: center;
    font: 700 37px/1 "Roboto", sans-serif;
    color: var(--slogan);
  }
  .soft-open {
    position: absolute; left: 455px; top: 195px;
    width: 250px; height: 26px; border-radius: 13px;
    background: var(--pill);
    display: flex; align-items: center; justify-content: center;
    font: 700 15px/1 "Montserrat", sans-serif;
    color: var(--ink);
  }
  .grand-opening {
    position: absolute; left: 0; right: 0; top: 226px;
    text-align: center;
    font: 400 50px/1.1 "Kaushan Script", cursive;
    color: var(--forest);
  }
  .grand-opening__date { color: var(--ink); }
  .divider {
    position: absolute; left: 349px; top: 299px;
    width: 460px; height: 2px;
    background: linear-gradient(90deg, var(--leaf) 0 62%, var(--forest) 62% 100%);
  }
  .location {
    position: absolute; left: 0; right: 0; top: 313px;
    display: flex; align-items: center; justify-content: center; gap: 12px;
    font: 600 16px/1 "Montserrat", sans-serif;
    color: var(--muted);
  }
  .location__pin { width: 12px; height: 16px; }
</style>
</head>
<body>
  <section class="billboard">
    <svg class="billboard__decor" viewBox="0 0 1160 341" aria-hidden="true">
      <g class="corner-shapes">
        <polygon points="0,0 14,0 232,214 125,341 0,341" fill="var(--forest)"/>
        <polygon points="14,0 48,0 262,212 232,214" fill="var(--leaf)"/>
        <polygon points="0,262 160,341 0,341" fill="var(--lime)"/>
        <polyline points="60,0 78,30 110,30 125,60" fill="none" stroke="var(--lime)" stroke-width="4"/>
      </g>
      <g class="corner-shapes" transform="translate(1160,0) scale(-1,1)">
        <polygon points="0,0 14,0 232,214 125,341 0,341" fill="var(--forest)"/>
        <polygon points="14,0 48,0 262,212 232,214" fill="var(--leaf)"/>
        <polygon points="0,262 160,341 0,341" fill="var(--lime)"/>
        <polyline points="60,0 78,30 110,30 125,60" fill="none" stroke="var(--lime)" stroke-width="4"/>
      </g>
      <g class="diamonds" fill="none" stroke="var(--pill)" stroke-width="4">
        <rect x="232" y="117" width="14" height="14" transform="rotate(45 239 124)"/>
        <rect x="24" y="156" width="14" height="14" transform="rotate(45 31 163)"/>
        <rect x="916" y="130" width="14" height="14" transform="rotate(45 923 137)"/>
        <rect x="1125" y="160" width="14" height="14" transform="rotate(45 1132 167)"/>
      </g>
      <g class="chevrons" fill="none" stroke="var(--forest)" stroke-width="5">
        <polyline points="115,0 140,20 165,0"/>
        <polyline points="995,0 1020,20 1045,0"/>
      </g>
      <g class="confetti" fill="var(--forest)">
        <rect x="303" y="27" width="7" height="6" transform="rotate(30 306 30)"/>
        <rect x="626" y="12" width="5" height="4"/>
        <rect x="955" y="24" width="7" height="6"/>
        <rect x="340" y="322" width="8" height="6" transform="rotate(20 344 325)"/>
      </g>
      <rect x="816" y="322" width="8" height="6" fill="var(--lime)" transform="rotate(35 820 325)"/>
    </svg>

    <div class="megaphone megaphone--left" role="img" aria-label="Pink megaphone illustration announcing the opening"></div>
    <div class="megaphone megaphone--right" role="img" aria-label="Pink megaphone illustration announcing the opening"></div>

    <h1 class="brand-name">Reed &amp; Vale</h1>
    <p class="slogan">Save Some Cash, Buy Our Grass</p>
    <p class="soft-open">OPEN STARTING AUG 1</p>
    <p class="grand-opening">Grand Opening <span class="grand-opening__date">Aug 15th</span></p>
    <div class="divider"></div>
    <p class="location">
      <svg class="location__pin" viewBox="0 0 12 16" aria-hidden="true">
        <path d="M6 0a6 6 0 0 0-6 6c0 4.5 6 10 6 10s6-5.5 6-10a6 6 0 0 0-6-6zm0 8.5A2.5 2.5 0 1 1 6 3.5a2.5 2.5 0 0 1 0 5z" fill="var(--slogan)"/>
      </svg>
      EXIT 4B MAPLECREST RD
    </p>
  </section>
</body>
</html>
```